Kestrel Flooring Supply

Basic one-sided business card design using the attached logo. Vintage americana theme. Font is modified Arial Nova Cond, but anything that coordinates can be used

```html
<!DOCTYPE html>
<html lang="en">
<head>
<meta charset="utf-8">
<title>Kestrel Flooring Supply – Business Card</title>
<link href="https://fonts.googleapis.com/css2?family=Arimo:wght@400;700&display=swap" rel="stylesheet">
<style>
  :root {
    --page-bg: #d9d1c6;
    --card-frost: #ece7e0;
    --card-edge: #f6f2ec;
    --panel-dark: #262321;
    --accent-gold: #a88456;
    --text-dark: #3b3835;
    --logo-cream: #ebe3d2;
  }
  * { margin: 0; padding: 0; box-sizing: border-box; }
  html, body {
    width: 1200px;
    height: 1047px;
    overflow: hidden;
    background: var(--page-bg);
    font-family: "Arimo", Arial, sans-serif;
  }
  .business-card {
    position: absolute;
    left: 100px;
    top: 250px;
    width: 1000px;
    height: 547px;
    border-radius: 18px;
    background: var(--card-frost);
    border: 2px solid var(--card-edge);
    overflow: hidden;
  }
  .brand-panel {
    position: absolute;
    inset: 0;
    width: 1000px;
    height: 547px;
  }
  .name-accent {
    position: absolute;
    left: 7px;
    top: 68px;
    width: 19px;
    height: 73px;
    background: var(--accent-gold);
  }
  .holder-name {
    position: absolute;
    left: 48px;
    top: 62px;
    font-size: 37px;
    font-weight: 700;
    letter-spacing: 0.5px;
    color: var(--accent-gold);
    line-height: 1;
  }
  .holder-title {
    position: absolute;
    left: 48px;
    top: 114px;
    font-size: 24px;
    color: var(--text-dark);
    line-height: 1;
  }
  .address {
    position: absolute;
    left: 48px;
    top: 222px;
    font-size: 25px;
    line-height: 39px;
    color: var(--text-dark);
    font-style: normal;
  }
  .contact-list {
    position: absolute;
    left: 48px;
    top: 368px;
    list-style: none;
    font-size: 24px;
    color: var(--text-dark);
  }
  .contact-list li {
    display: flex;
    align-items: center;
    height: 38px;
  }
  .contact-icon {
    width: 20px;
    height: 20px;
    margin-right: 12px;
    fill: var(--text-dark);
  }
  .brand-name {
    position: absolute;
    left: 500px;
    top: 190px;
    width: 480px;
    text-align: center;
    color: var(--logo-cream);
    font-weight: 700;
    font-size: 44px;
    line-height: 58px;
    letter-spacing: 2px;
    text-transform: uppercase;
  }
</style>
</head>
<body>
  <main class="business-card">
    <svg class="brand-panel" viewBox="0 0 1000 547" aria-hidden="true">
      <path fill="var(--panel-dark)" d="M661 0 H982 Q1000 0 1000 18 V529 Q1000 547 982 547 H672 C540 547 440 430 440 273 C440 120 535 0 661 0 Z"/>
    </svg>

    <div class="name-accent"></div>
    <h1 class="holder-name">DANIEL HARTLEY</h1>
    <p class="holder-title">Managing Director</p>

    <address class="address">Your address, City<br>State, Zip 1234</address>

    <ul class="contact-list">
      <li>
        <svg class="contact-icon" viewBox="0 0 20 20" aria-hidden="true"><path d="M2 7 Q10 1 18 7 L16 10 L13 8 L13 6 Q10 5 7 6 L7 8 L4 10 Z M4 11 H16 V17 H4 Z"/></svg>
        123 456 789
      </li>
      <li>
        <svg class="contact-icon" viewBox="0 0 20 20" aria-hidden="true"><path d="M2 5 H18 V16 H2 Z M3.5 6.5 L10 11 L16.5 6.5 V7.8 L10 12.4 L3.5 7.8 Z" fill-rule="evenodd"/></svg>
        info@kestrelfloors.com
      </li>
      <li>
        <svg class="contact-icon" viewBox="0 0 20 20" aria-hidden="true"><circle cx="10" cy="10" r="8"/><path d="M6 6 Q9 5 10 8 Q8 11 5 10 Z M12 11 Q15 10 15 14 Q13 16 11 14 Z" fill="var(--card-frost)"/></svg>
        www.kestrelfloors.com
      </li>
    </ul>

    <p class="brand-name">Kestrel<br>Flooring Supply</p>
  </main>
</body>
</html>
```